Corridor Works

Small ageny public transit advocacy, funding and compliance.
Consulting and lobbying efforts for small public transit agencies and communities exploring public transit opportunities.

I was interested in a simple line sketch suggesting motion, mobility. The card will be black on white. I would like it to include the bUs ones brief; Advocacy, Funding , and Compliance for small transit agencies.

Reason: I have been traveling and have had limited time to respond. Thank you all for your submit talks.

Industry/Entity Type

Consulting

Contact Information for Business Card

Paul R Vesby
Phone (907) 418-2960
Email paulrvesby@mailnook.net

```html
<!DOCTYPE html>
<html lang="en">
<head>
<meta charset="utf-8">
<title>Corridor Works — Business Card</title>
<link href="https://fonts.googleapis.com/css2?family=Cinzel:wght@400&family=Crimson+Text:wght@400&display=swap" rel="stylesheet">
<style>
  :root {
    --backdrop: #3b3e40;
    --card: #ffffff;
    --frame: #a9a9a9;
    --mark: #8c8c8c;
    --ink: #1c1c1c;
  }
  html, body {
    margin: 0;
    width: 1200px;
    height: 1000px;
    overflow: hidden;
    background: var(--backdrop);
  }
  .card {
    position: absolute;
    left: 170px;
    top: 250px;
    width: 860px;
    height: 500px;
    background: var(--card);
  }
  .card__frame {
    position: absolute;
    inset: 32px 32px 33px 40px;
    border: 3px solid var(--frame);
  }
  .brand {
    position: absolute;
    left: 0;
    right: 0;
    top: 140px;
    display: flex;
    justify-content: center;
    align-items: center;
    gap: 14px;
  }
  .brand__square {
    width: 14px;
    height: 14px;
    background: var(--mark);
  }
  .brand__name {
    font-family: "Cinzel", serif;
    font-size: 34px;
    letter-spacing: 4px;
    color: var(--mark);
  }
  .holder {
    position: absolute;
    left: 0;
    right: 0;
    top: 350px;
    text-align: center;
    font-family: "Cinzel", serif;
    font-size: 40px;
    color: var(--ink);
    letter-spacing: 1px;
  }
  .contact {
    position: absolute;
    left: 0;
    right: 0;
    top: 412px;
    display: flex;
    justify-content: center;
    align-items: center;
    gap: 12px;
    font-family: "Crimson Text", serif;
    font-size: 21px;
    color: var(--ink);
  }
  .contact__item {
    display: flex;
    align-items: center;
    gap: 8px;
  }
  .contact__icon {
    width: 18px;
    height: 18px;
  }
</style>
</head>
<body>
  <div class="card">
    <div class="card__frame"></div>

    <div class="brand">
      <span class="brand__square"></span>
      <span class="brand__name">Corridor Works</span>
    </div>

    <div class="holder">Paul R Vesby</div>

    <div class="contact">
      <span class="contact__item">
        <svg class="contact__icon" viewBox="0 0 20 20" aria-hidden="true">
          <circle cx="10" cy="10" r="10" fill="#1c1c1c"/>
          <path d="M6.2 5.2 L8 5 L9 7.6 L7.9 8.5 C8.5 9.9 9.8 11.3 11.4 12 L12.3 10.9 L14.9 11.9 L14.7 13.7 C14.6 14.3 14 14.8 13.3 14.7 C9.4 14.2 5.7 10.5 5.2 6.6 C5.1 5.9 5.6 5.3 6.2 5.2 Z" fill="#ffffff"/>
        </svg>
        (907) 418-2960
      </span>
      <span class="contact__item">
        <svg class="contact__icon" viewBox="0 0 20 20" aria-hidden="true">
          <circle cx="10" cy="10" r="10" fill="#1c1c1c"/>
          <rect x="5" y="6.5" width="10" height="7" fill="#ffffff"/>
          <path d="M5 6.5 L10 10.5 L15 6.5" fill="none" stroke="#1c1c1c" stroke-width="1.2"/>
        </svg>
        paulrvesby@mailnook.net
      </span>
    </div>
  </div>
</body>
</html>
```